Business Card Design Project

Name: Femi C. Okoro
Designation: Partner
Address: KPR Building, 14 Marigold Close, P.O. Box 58314, Victoria Island Lagos, Nigeria
Tel: +234 1 5937261
mobile: +234 1 7069514372
Email: fcokoro@brackenhillpartners.com
website www.brackenhillpartners.com

```html
<!DOCTYPE html>
<html lang="en">
<head>
<meta charset="UTF-8">
<title>Brackenhill Partners – Business Card</title>
<link rel="stylesheet" href="https://fonts.googleapis.com/css2?family=Open+Sans:wght@400;600&display=swap">
<style>
  :root {
    --stage: #dfe3e5;
    --card-white: #ffffff;
    --band-grey: #6a6a6a;
    --ink-dark: #1c1c1c;
    --ink-light: #ffffff;
    --mark-grey: #5a5a5a;
  }
  * { margin: 0; padding: 0; box-sizing: border-box; }
  html, body { width: 1200px; height: 960px; overflow: hidden; }
  body {
    background: var(--stage);
    font-family: "Open Sans", Arial, sans-serif;
    position: relative;
  }
  .card {
    position: absolute;
    left: 285px;
    width: 630px;
    height: 360px;
    background: var(--card-white);
    box-shadow: 0 6px 18px rgba(0,0,0,0.18);
    overflow: hidden;
  }
  .card--front { top: 90px; }
  .card--back { top: 510px; }

  .brand {
    position: absolute;
    display: flex;
    align-items: center;
    gap: 18px;
  }
  .brand__square {
    width: 72px;
    height: 72px;
    background: var(--mark-grey);
  }
  .brand__name {
    font-weight: 600;
    color: var(--ink-dark);
    font-size: 34px;
    line-height: 1.05;
  }
  .card--front .brand { left: 34px; top: 38px; }

  .info-band {
    position: absolute;
    left: 0; right: 0; bottom: 0;
    height: 210px;
    background: var(--band-grey);
    color: var(--ink-light);
  }
  .person { position: absolute; left: 30px; top: 22px; }
  .person__name { font-size: 30px; font-weight: 400; letter-spacing: 0.2px; }
  .person__title { font-size: 16px; margin-top: 6px; margin-left: 10px; }
  .address {
    position: absolute; left: 30px; top: 118px;
    font-size: 13px; line-height: 1.4;
  }
  .phones {
    position: absolute; left: 345px; top: 18px;
    display: flex; align-items: center; gap: 16px;
  }
  .phones__list { font-size: 19px; line-height: 1.35; letter-spacing: 0.5px; }
  .contact-line {
    position: absolute;
    display: flex; align-items: center; gap: 8px;
    font-size: 13px;
    letter-spacing: 0.3px;
  }
  .contact-line--web { left: 345px; top: 124px; }
  .contact-line--mail { left: 48px; bottom: 20px; }

  .card--back .brand { left: 150px; top: 90px; }
  .card--back .brand__square { width: 96px; height: 96px; }
  .card--back .brand__name { font-size: 40px; }
  .back-web {
    position: absolute; left: 0; right: 0; top: 240px;
    text-align: center;
    font-size: 28px; font-weight: 600;
    color: var(--ink-dark);
  }
</style>
</head>
<body>

<section class="card card--front">
  <div class="brand">
    <div class="brand__square"></div>
    <div class="brand__name">Brackenhill<br>Partners</div>
  </div>

  <div class="info-band">
    <div class="person">
      <div class="person__name">Femi C. Okoro</div>
      <div class="person__title">Partner</div>
    </div>

    <div class="address">
      KPR Building, 14 Marigold Close,<br>
      P.O. Box 58314, Victoria Island Lagos, Nigeria
    </div>

    <div class="phones">
      <svg width="34" height="40" viewBox="0 0 34 40" aria-hidden="true">
        <path d="M9 2 L14 12 L10 16 C12 22 16 27 21 30 L25 26 L33 32 L29 38 C16 36 4 22 3 8 Z" fill="#ffffff"/>
      </svg>
      <div class="phones__list">
        +234 1 5937261<br>
        +234 1 7069514372
      </div>
    </div>

    <div class="contact-line contact-line--web">
      <svg width="16" height="16" viewBox="0 0 16 16" aria-hidden="true">
        <circle cx="8" cy="8" r="6.5" fill="none" stroke="#fff" stroke-width="1.4"/>
        <ellipse cx="8" cy="8" rx="3" ry="6.5" fill="none" stroke="#fff" stroke-width="1"/>
        <line x1="1.5" y1="8" x2="14.5" y2="8" stroke="#fff" stroke-width="1"/>
      </svg>
      <span>brackenhillpartners.com</span>
    </div>

    <div class="contact-line contact-line--mail">
      <svg width="24" height="17" viewBox="0 0 24 17" aria-hidden="true">
        <rect x="0.5" y="0.5" width="23" height="16" fill="#fff"/>
        <polyline points="1,1 12,10 23,1" fill="none" stroke="#6a6a6a" stroke-width="1.4"/>
      </svg>
      <span>fcokoro@brackenhillpartners.com</span>
    </div>
  </div>
</section>

<section class="card card--back">
  <div class="brand">
    <div class="brand__square"></div>
    <div class="brand__name">Brackenhill<br>Partners</div>
  </div>
  <div class="back-web">www.brackenhillpartners.com</div>
</section>

</body>
</html>
```